Business Card - Cooperate

Business Card for Larkfield Management Consulting

Target Market(s)

Corparte - b2B

Industry/Entity Type

Management Consulting - Professional Services

Contact Information for Business Card

Company Name , Slogan , Dummy Address,

Requirements
Must have
• BUILD WHAT COMES NEXT

```html
<!DOCTYPE html>
<html lang="en">
<head>
<meta charset="utf-8">
<title>Larkfield Management Consulting – Business Card</title>
<link rel="stylesheet" href="https://fonts.googleapis.com/css2?family=Montserrat:wght@400;500;600;700&display=swap">
<style>
  :root{
    --backdrop:#e9eaec;
    --paper:#ffffff;
    --front-light:#2143b8;
    --front-dark:#151b78;
    --ink:#1b1b1f;
    --icon-blue:#1a56d6;
    --brand-navy:#1c2a8f;
    --brand-blue:#2d6cf0;
    --slogan-teal:#1a9c80;
    --slogan-blue:#3a63dc;
  }
  *{margin:0;padding:0;box-sizing:border-box}
  html,body{width:939px;height:1200px;overflow:hidden}
  body{background:var(--backdrop);font-family:'Montserrat',sans-serif;position:relative}

  .card{position:absolute;left:155px;width:646px;height:418px;overflow:hidden}
  .card--front{top:138px;background:linear-gradient(90deg,var(--front-light) 0%,var(--front-dark) 100%)}
  .card--back{top:627px;background:var(--paper)}

  .pattern-area{position:absolute;left:70px;top:8px;width:560px;height:400px;
    background:linear-gradient(90deg,rgba(60,100,220,0.10),rgba(70,110,230,0.28));border-radius:6px}

  .brand{position:absolute;display:flex;flex-direction:column}
  .brand__row{display:flex;align-items:center;gap:12px}
  .brand__dot{width:50px;height:50px;border-radius:50%;flex:none}
  .brand__name{font-weight:600;font-size:36px;line-height:1;letter-spacing:0.5px}
  .brand__slogan{font-weight:700;font-size:8px;letter-spacing:1.3px;margin-left:62px;margin-top:2px;white-space:nowrap}

  .card--front .brand{left:393px;top:337px}
  .card--front .brand__dot{background:var(--brand-blue)}
  .card--front .brand__name{color:var(--brand-blue)}
  .card--front .brand__slogan{color:var(--slogan-blue)}

  .card--back .brand{left:380px;top:323px}
  .card--back .brand__dot{width:54px;height:54px;background:var(--icon-blue)}
  .card--back .brand__name{color:var(--brand-navy)}
  .card--back .brand__slogan{color:var(--slogan-teal)}

  .holder-name{position:absolute;right:34px;top:40px;font-size:28px;line-height:34px;color:var(--ink);letter-spacing:0.3px;white-space:nowrap}
  .holder-name__first{font-weight:700}
  .holder-name__last{font-weight:400}
  .name-rule{position:absolute;left:508px;right:0;top:80px;height:2px;background:var(--ink)}

  .contact{position:absolute;left:42px;display:flex;align-items:flex-start;gap:11px;
    font-size:18px;color:var(--ink);line-height:23px;white-space:nowrap}
  .contact svg{flex:none;width:25px;height:25px}
  .contact--address{top:207px}
  .contact--phone{top:287px}
  .contact--email{top:323px}
  .contact--web{top:359px}
  .contact-rule{position:absolute;left:0;width:283px;top:266px;height:2px;background:var(--ink)}
</style>
</head>
<body>

<section class="card card--front" aria-label="Card front">
  <div class="pattern-area" role="img" aria-label="Faint repeating brand-mark pattern across the card"></div>
  <div class="brand">
    <div class="brand__row"><span class="brand__dot"></span><span class="brand__name">Larkfield</span></div>
    <span class="brand__slogan">BUILD WHAT COMES NEXT</span>
  </div>
</section>

<section class="card card--back" aria-label="Card back">
  <h1 class="holder-name"><span class="holder-name__first">DARIA</span> <span class="holder-name__last">WELTON</span></h1>
  <div class="name-rule"></div>

  <div class="contact contact--address">
    <svg viewBox="0 0 26 26"><circle cx="13" cy="13" r="11.5" fill="none" stroke="var(--icon-blue)" stroke-width="1.8"/><path d="M13 6.5a4.3 4.3 0 0 0-4.3 4.3c0 3.2 4.3 8 4.3 8s4.3-4.8 4.3-8A4.3 4.3 0 0 0 13 6.5z" fill="var(--icon-blue)"/><circle cx="13" cy="10.8" r="1.6" fill="#fff"/></svg>
    <p>42 Harlow Street, Suite#3<br>Brookvale, NY -118</p>
  </div>
  <div class="contact-rule"></div>

  <div class="contact contact--phone">
    <svg viewBox="0 0 26 26"><circle cx="13" cy="13" r="11.5" fill="none" stroke="var(--icon-blue)" stroke-width="1.8"/><path d="M9.2 7.5l2 .2 1 3-1.4 1.1a8 8 0 0 0 3.4 3.4l1.1-1.4 3 1 .2 2c-.3 1-1.3 1.6-2.4 1.4C11.6 17.6 8.4 14.4 7.8 9.9c-.2-1.1.4-2.1 1.4-2.4z" fill="var(--icon-blue)"/></svg>
    <p>917 . 408&nbsp; 26153740</p>
  </div>

  <div class="contact contact--email">
    <svg viewBox="0 0 26 26"><circle cx="13" cy="13" r="11.5" fill="none" stroke="var(--icon-blue)" stroke-width="1.8"/><rect x="7.5" y="9" width="11" height="8" rx="1" fill="var(--icon-blue)"/><path d="M7.8 9.5l5.2 4 5.2-4" fill="none" stroke="#fff" stroke-width="1.1"/></svg>
    <p>hello@dariawelton.com</p>
  </div>

  <div class="contact contact--web">
    <svg viewBox="0 0 26 26"><circle cx="13" cy="13" r="11.5" fill="none" stroke="var(--icon-blue)" stroke-width="1.8"/><path d="M10 7.5l7.5 7-3.4.4 2 3.8-1.5.8-2-3.8-2.6 2.3z" fill="var(--icon-blue)"/></svg>
    <p>www.dariawelton.com</p>
  </div>

  <div class="brand">
    <div class="brand__row"><span class="brand__dot"></span><span class="brand__name">Larkfield</span></div>
    <span class="brand__slogan">BUILD WHAT COMES NEXT</span>
  </div>
</section>

</body>
</html>
```